Redesign the *Settings* screen for the PelikoZ app.

PelikoZ app is in production, but we need to refresh and redesign the settings screen to be cleaner, easier, more intuitive, and more professional looking.

Project Deadline Extended
Reason: Several designers have requested more time. This will also give time to provide feedback on existing designs.

Requirements
Must have
• Black background, so that the screen is consistent with the rest of the app.

```html
<!DOCTYPE html>
<html lang="en">
<head>
<meta charset="utf-8">
<title>PelikoZ Settings</title>
<link href="https://fonts.googleapis.com/css2?family=Dosis:wght@700;800&display=swap" rel="stylesheet">
<style>
  :root {
    --bg-black: #111111;
    --accent-red: #c4262e;
    --tile-grey: #dcdcdc;
    --tile-light: #efefef;
    --text-light: #e6e6e6;
    --text-dark: #111111;
    --white: #ffffff;
  }
  * { margin: 0; padding: 0; box-sizing: border-box; }
  html, body { width: 1200px; height: 3072px; overflow: hidden; background: var(--white); }
  body { font-family: "Dosis", sans-serif; font-weight: 700; }
  .settings { position: relative; width: 1200px; height: 3072px; }
  .band { position: absolute; left: 0; width: 1200px; background: var(--bg-black); }
  .heading {
    position: absolute; left: 86px; color: var(--text-light);
    font-size: 86px; line-height: 1; transform: translateY(-50%); letter-spacing: 1px;
  }
  .current-value {
    position: absolute; left: 86px; color: var(--accent-red);
    font-size: 66px; line-height: 1; transform: translateY(-50%);
  }
  .option-row { position: absolute; left: 0; width: 1200px; display: flex; }
  .option { position: relative; flex: 1; height: 100%; }
  .option.is-active { background: var(--accent-red); color: var(--white); }
  .option.is-idle { background: var(--tile-grey); color: var(--text-dark); }
  .option.is-light { background: var(--tile-light); color: var(--text-dark); }
  .option-label {
    position: absolute; left: 0; right: 0; text-align: center;
    font-size: 72px; line-height: 1; transform: translateY(-50%);
  }
  .option-icon { position: absolute; left: 50%; transform: translate(-50%, -50%); }
  .icon-fill-light { background: var(--white); }
  .icon-fill-dark { background: var(--text-dark); }
  .co2 {
    position: absolute; left: 0; right: 0; top: 50%; transform: translateY(-50%);
    text-align: center; font-size: 150px; font-weight: 800; line-height: 1;
  }
  .co2 sub { font-size: 80px; vertical-align: -0.35em; }
</style>
</head>
<body>
<main class="settings">
  <section class="band" style="top:0;height:333px">
    <h2 class="heading" style="top:256px">WEAPON</h2>
  </section>

  <div class="option-row" style="top:333px;height:601px">
    <div class="option is-active">
      <div class="option-icon icon-fill-light" role="img" aria-label="Pistol icon" style="top:278px;width:190px;height:140px;border-radius:10px"></div>
      <span class="option-label" style="top:470px">PISTOL</span>
    </div>
    <div class="option is-idle">
      <div class="option-icon icon-fill-dark" role="img" aria-label="Rifle icon" style="top:278px;width:290px;height:90px;border-radius:10px"></div>
      <span class="option-label" style="top:470px">RIFLE</span>
    </div>
  </div>

  <section class="band" style="top:934px;height:613px">
    <h2 class="heading" style="top:202px">CURRENT FIREARM</h2>
    <p class="current-value" style="top:327px">K240</p>
    <h2 class="heading" style="top:538px">HAND</h2>
  </section>

  <div class="option-row" style="top:1546px;height:601px">
    <div class="option is-active">
      <div class="option-icon icon-fill-light" role="img" aria-label="Left hand icon" style="top:268px;width:125px;height:185px;border-radius:30px 30px 40px 40px"></div>
      <span class="option-label" style="top:470px">LEFT</span>
    </div>
    <div class="option is-idle">
      <div class="option-icon icon-fill-dark" role="img" aria-label="Right hand icon" style="top:268px;width:125px;height:185px;border-radius:30px 30px 40px 40px"></div>
      <span class="option-label" style="top:470px">RIGHT</span>
    </div>
  </div>

  <section class="band" style="top:2147px;height:320px">
    <h2 class="heading" style="top:247px">PRACTICE</h2>
  </section>

  <div class="option-row" style="top:2467px;height:381px">
    <div class="option is-active">
      <div class="option-icon icon-fill-light" role="img" aria-label="Cartridge icon" style="top:157px;width:108px;height:192px;border-radius:54px 54px 6px 6px"></div>
      <span class="option-label" style="top:317px">LIVE FIRE</span>
    </div>
    <div class="option is-idle">
      <svg class="option-icon" style="top:141px" width="190" height="190" viewBox="0 0 190 190" aria-hidden="true">
        <circle cx="95" cy="95" r="84" fill="none" stroke="var(--text-dark)" stroke-width="8"/>
        <line x1="36" y1="36" x2="154" y2="154" stroke="var(--text-dark)" stroke-width="8"/>
        <line x1="154" y1="36" x2="36" y2="154" stroke="var(--text-dark)" stroke-width="8"/>
      </svg>
      <span class="option-label" style="top:317px">DRY FIRE</span>
    </div>
    <div class="option is-light">
      <span class="co2">CO<sub>2</sub></span>
    </div>
  </div>
</main>
</body>
</html>
```